Seeking a beautiful packaging box for Dusk Haven - an essential oil blend (mock up provided!)

My sleep brand - Dusk Haven - is almost ready to go to market. And I need a box! Dusk Haven is a high end essential oils/sleep hygiene brand.

I need a gorgeous, classy box for our 3 sizes of essential oil product we are selling. I have a draft mockup which is to approximate size (attached), but need some help with the finishing touches and layout so it's really polished. I am looking for simple/monochrome designs using black and off white (think Verlin inspo!)

We are selling a 15mL dropper bottle and two roll ons (5ml, 10ml) of the essential oil blend. These are all amber bottles with black top. The box design will be almost identical for each, with very slight variations due to size differences.

The size of the boxes will be
15mL dropper: 30x30x95mm
10ml roller: 19x19x88mm
5ml roller: 18x18x59mm

Target Market(s)

High end/high price point product, shift workers, mums, people suffering stress and insomnia

Industry/Entity Type

Health And Wellness

Font styles to use
Serif
Sans Serif

Colors

Designer to choose only greyscale colors for use in the design.

Requirements
Must have
• I have attached a word document which includes all the necessary text:
- ingredients
- directions
- cautions
- info on essential oils/dusk haven (abbreviated on the smallest box)

Additionally:
- volume
- our website
- instagram logo/duskhavenau name
- made in australia
- recycle symbol
- 12 month open symbol
Nice to have
• I would like the boxes to be monochromatic: white or off white colour, with black logo and writing. I am open to variations on the logo (ie position of writing in relation to the circle/change of font size), but mostly need help with layout, font, direction of text, design of the blank spaces, patterns etc.
Should not have
• Colours

```html
<!DOCTYPE html>
<html lang="en">
<head>
<meta charset="utf-8">
<title>Dusk Haven – Essential Oil Box Dielines</title>
<link rel="stylesheet" href="https://fonts.googleapis.com/css2?family=Josefin+Sans:wght@300;400;600&display=swap">
<style>
  :root {
    --paper: #ffffff;
    --ink: #111111;
    --fold: #d8d8d8;
    --reverse: #ffffff;
  }
  html, body { margin: 0; padding: 0; background: var(--paper); overflow: hidden; }
  .canvas { width: 1200px; height: 720px; overflow: hidden; background: var(--paper); }
  .canvas svg { display: block; }
  .dieline { fill: none; stroke: var(--ink); stroke-width: 2.5; stroke-linejoin: round; }
  .fold { fill: none; stroke: var(--fold); stroke-width: 1.5; }
  .tab-ring { fill: none; stroke: var(--ink); }
  .brand-dot { fill: none; stroke: var(--ink); }
  .copy { font-family: "Josefin Sans", sans-serif; font-weight: 300; fill: var(--ink); }
  .copy.center { text-anchor: middle; }
  .brand { font-family: "Josefin Sans", sans-serif; font-weight: 400; fill: var(--ink); }
  .brand.center { text-anchor: middle; }
  .strong { font-weight: 600; }
  .label-bar { fill: var(--ink); }
  .bar-text { font-family: "Josefin Sans", sans-serif; font-weight: 400; fill: var(--reverse); }
  .bar-text.center { text-anchor: middle; }
  .icon-line { fill: none; stroke: var(--ink); }
  .icon-text { font-family: "Josefin Sans", sans-serif; font-weight: 600; fill: var(--ink); text-anchor: middle; }
</style>
</head>
<body>
<div class="canvas">
<svg width="1200" height="720" viewBox="0 0 2480 1488" xmlns="http://www.w3.org/2000/svg">
  <defs>
    <symbol id="open-jar" viewBox="0 0 60 50">
      <ellipse class="icon-line" cx="32" cy="11" rx="24" ry="5.5" transform="rotate(-12 32 11)" stroke-width="3"/>
      <path class="icon-line" d="M6 24 h48 v16 a6 6 0 0 1 -6 6 h-36 a6 6 0 0 1 -6 -6z" stroke-width="3"/>
      <text class="icon-text" x="30" y="41" font-size="13">12M</text>
    </symbol>
    <symbol id="recycle-mark" viewBox="0 0 60 60">
      <circle class="icon-line" cx="30" cy="30" r="27" stroke-width="3"/>
      <polygon class="icon-line" points="30,15 44,39 16,39" stroke-width="4" stroke-linejoin="round"/>
    </symbol>
  </defs>

  <!-- ================= 15 mL dropper box ================= -->
  <g class="box box-15ml">
    <path class="dieline" d="M348,385 V120 Q348,108 360,108 H562 Q574,108 574,120 V385
      M348,242 H176 L137,368 Q122,372 122,385 L65,410 V1075 L122,1098 Q122,1110 137,1115 L176,1240 H348
      M348,1098 V1363 Q348,1375 360,1375 H562 Q574,1375 574,1363 V1098
      M574,242 H745 L785,368 Q798,372 798,385
      M574,1240 H745 L785,1115 Q798,1110 798,1098
      M348,160 h17 M557,160 h17 M348,1322 h17 M557,1322 h17"/>
    <rect class="dieline" x="798" y="385" width="226" height="713"/>
    <circle class="tab-ring" cx="461" cy="272" r="72" stroke-width="10"/>
    <circle class="tab-ring" cx="461" cy="1212" r="72" stroke-width="10"/>

    <!-- ingredients panel -->
    <g class="panel-ingredients">
      <circle class="brand-dot" cx="177" cy="1010" r="28" stroke-width="5"/>
      <text class="brand" transform="translate(172,968) rotate(-90)" font-size="40" letter-spacing="2">
        <tspan x="0" y="0">DUSK</tspan><tspan x="0" dy="36">HAVEN</tspan>
      </text>
      <rect class="label-bar" x="228" y="855" width="19" height="185"/>
      <text class="bar-text" transform="translate(243,1035) rotate(-90)" font-size="14">INGREDIENTS:</text>
      <text class="copy" transform="translate(270,1040) rotate(-90)" font-size="13">
        <tspan x="0" y="0">Lavandula Angustifolia (Australian Lavender), Vetiveria Zizanoides (Vetiver) Root Oil, Sweet Vanilla</tspan>
        <tspan x="0" dy="18.5">Fragrant Oil, Pelargonium Capitatum (Cape Rose Geranium) Leaf Extract, Juniperus Virginiana</tspan>
        <tspan x="0" dy="18.5">(Cedarwood) Wood Oil, Citrus Limon (Australian Lemon) Peel Oil, Origanum Majorana (Marjoram)</tspan>
        <tspan x="0" dy="18.5">Leaf Oil, Cananga Odorata (Ylang Ylang) Flower Oil, Anthemis Nobilis (Roman Chamomile) Flower Oil.</tspan>
      </text>
    </g>

    <!-- front panel -->
    <g class="panel-front">
      <circle class="brand-dot" cx="461" cy="587" r="48" stroke-width="7"/>
      <text class="brand center" x="461" y="705" font-size="58" letter-spacing="3">DUSK</text>
      <text class="brand center" x="461" y="736" font-size="26" letter-spacing="15">HAVEN</text>
      <rect class="label-bar" x="367" y="764" width="187" height="24"/>
      <text class="bar-text center" x="461" y="783" font-size="20">Essential Oil Blend</text>
      <text class="copy center" x="461" y="1013" font-size="20">Made in Australia</text>
      <text class="copy center" x="461" y="1043" font-size="20">15mL / 1/2 fl. oz</text>
    </g>

    <!-- directions panel -->
    <g class="panel-directions">
      <rect class="label-bar" x="591" y="443" width="188" height="19"/>
      <text class="bar-text" x="599" y="458" font-size="14">DIRECTIONS:</text>
      <text class="copy center" font-size="14">
        <tspan x="686" y="484">DIFFUSE</tspan>
        <tspan x="686" dy="17.5">Add 4-6 drops to a diffuser or</tspan>
        <tspan x="686" dy="17.5">oilburner at night to create</tspan>
        <tspan x="686" dy="17.5">a calm and grounded</tspan>
        <tspan x="686" dy="17.5">environment.</tspan>
        <tspan x="686" dy="35">BATHE</tspan>
        <tspan x="686" dy="17.5">Add 2-4 drops to a warm bath</tspan>
        <tspan x="686" dy="17.5">to help calm the body and</tspan>
        <tspan x="686" dy="17.5">mind.</tspan>
        <tspan x="686" dy="35">INHALE</tspan>
        <tspan x="686" dy="17.5">Place 2 drops in the palms of</tspan>
        <tspan x="686" dy="17.5">the hands and inhale directly to</tspan>
        <tspan x="686" dy="17.5">ease you into a restful sleep.</tspan>
        <tspan x="686" dy="35">MASSAGE</tspan>
        <tspan x="686" dy="17.5">Dilute 4 drops with a carrier oil</tspan>
        <tspan x="686" dy="17.5">(such as jojoba or coconut), and</tspan>
        <tspan x="686" dy="17.5">massage into the feet before</tspan>
        <tspan x="686" dy="17.5">sleep.</tspan>
      </text>
      <rect class="label-bar" x="591" y="857" width="188" height="20"/>
      <text class="bar-text" x="599" y="872" font-size="14">CAUTION:</text>
      <text class="copy center" font-size="14">
        <tspan x="686" y="899">Possible skin sensitivity. Keep</tspan>
        <tspan x="686" dy="17.5">out of reach of children. Not for</tspan>
        <tspan x="686" dy="17.5">ingestion or internal use. Avoid</tspan>
        <tspan x="686" dy="17.5">contact with eyes, inner ears</tspan>
        <tspan x="686" dy="17.5">and sensitive areas.</tspan>
      </text>
      <circle class="brand-dot" cx="630" cy="1020" r="19" stroke-width="4"/>
      <text class="brand" x="660" y="1016" font-size="25" letter-spacing="1">DUSK</text>
      <text class="brand" x="660" y="1042" font-size="25" letter-spacing="1">HAVEN</text>
    </g>

    <!-- info panel -->
    <g class="panel-info">
      <text class="copy center" font-size="14">
        <tspan x="911" y="452">Essential Oils have been used</tspan>
        <tspan x="911" dy="17.5">for centuries to help prepare</tspan>
        <tspan x="911" dy="17.5">the mind and body for sleep.</tspan>
        <tspan x="911" dy="35">Dusk Haven contain a</tspan>
        <tspan x="911" dy="17.5">balanced blend of the most</tspan>
        <tspan x="911" dy="17.5">sleep supporting essential oils.</tspan>
        <tspan x="911" dy="35"><tspan class="strong">Lavender</tspan> for restfulness</tspan>
        <tspan x="911" dy="18"><tspan class="strong">Vetiver</tspan> for grounding</tspan>
        <tspan x="911" dy="18"><tspan class="strong">Cedarwood</tspan> for relaxation</tspan>
        <tspan x="911" dy="18"><tspan class="strong">Marjoram</tspan> for balance</tspan>
        <tspan x="911" dy="18"><tspan class="strong">Roman Chamomile</tspan> for comfort</tspan>
        <tspan x="911" dy="35">Add Dusk Haven to your</tspan>
        <tspan x="911" dy="17.5">nightly bedtime ritual to help</tspan>
        <tspan x="911" dy="17.5">support you in achieving deep</tspan>
        <tspan x="911" dy="17.5">and rejuvenating sleep.</tspan>
      </text>
      <rect class="brand-dot" x="886" y="783" width="50" height="50" stroke-width="5"/>
      <text class="copy center" x="911" y="853" font-size="17">@duskhavenau</text>
      <text class="copy center" x="911" y="903" font-size="17">Visit</text>
      <rect class="label-bar" x="817" y="907" width="187" height="20"/>
      <text class="bar-text center" x="911" y="923" font-size="15">www.duskhaven.com.au</text>
      <text class="copy center" x="911" y="943" font-size="17">to learn more</text>
      <use href="#open-jar" x="845" y="985" width="60" height="50"/>
      <use href="#recycle-mark" x="919" y="988" width="55" height="55"/>
    </g>
  </g>

  <!-- ================= 10 mL roll-on box ================= -->
  <g class="box box-10ml">
    <path class="dieline" d="M1314,412 V248 Q1314,236 1326,236 H1445 Q1457,236 1457,248 V412
      M1314,321 H1205 L1185,400 Q1172,404 1172,412 L1118,437 V1050 L1172,1072 Q1172,1080 1185,1084 L1205,1163 H1314
      M1314,1072 V1236 Q1314,1248 1326,1248 H1445 Q1457,1248 1457,1236 V1072
      M1457,321 H1566 L1586,400 Q1600,404 1600,412
      M1457,1163 H1566 L1586,1084 Q1600,1080 1600,1072
      M1314,272 h12 M1445,272 h12 M1314,1213 h12 M1445,1213 h12"/>
    <path class="fold" d="M1172,412 H1600 M1172,1072 H1600"/>
    <rect class="dieline" x="1600" y="412" width="143" height="660"/>
    <circle class="tab-ring" cx="1385" cy="340" r="42" stroke-width="7"/>
    <circle class="tab-ring" cx="1385" cy="1143" r="42" stroke-width="7"/>

    <g class="panel-ingredients">
      <circle class="brand-dot" cx="1202" cy="1028" r="15" stroke-width="3.5"/>
      <text class="brand" transform="translate(1199,1002) rotate(-90)" font-size="24" letter-spacing="1">
        <tspan x="0" y="0">DUSK</tspan><tspan x="0" dy="22">HAVEN</tspan>
      </text>
      <rect class="label-bar" x="1228" y="878" width="15" height="164"/>
      <text class="bar-text" transform="translate(1240,1038) rotate(-90)" font-size="11">INGREDIENTS:</text>
      <text class="copy" transform="translate(1261,1042) rotate(-90)" font-size="10">
        <tspan x="0" y="0">Lavandula Angustifolia (Australian Lavender), Vetiveria Zizanoides (Vetiver) Root Oil, Sweet Vanilla Fragrant Oil, Pelargonium</tspan>
        <tspan x="0" dy="12.5">Capitatum (Cape Rose Geranium) Leaf Extract, Juniperus Virginiana (Cedarwood) Wood Oil, Citrus Limon (Australian Lemon) Peel</tspan>
        <tspan x="0" dy="12.5">Oil, Origanum Majorana (Marjoram) Leaf Oil, Cananga Odorata (Ylang Ylang) Flower Oil, Anthemis Nobilis (Roman Chamomile)</tspan>
        <tspan x="0" dy="12.5">Flower Oil.</tspan>
      </text>
    </g>

    <g class="panel-front">
      <circle class="brand-dot" cx="1385" cy="660" r="30" stroke-width="5"/>
      <text class="brand center" x="1385" y="733" font-size="38" letter-spacing="2">DUSK</text>
      <text class="brand center" x="1385" y="756" font-size="16" letter-spacing="9">HAVEN</text>
      <text class="copy center" x="1385" y="792" font-size="14">Roll on</text>
      <rect class="label-bar" x="1327" y="796" width="117" height="14"/>
      <text class="bar-text center" x="1385" y="807" font-size="12">Essential Oil Blend</text>
      <text class="copy center" x="1385" y="1024" font-size="14">Made in Australia</text>
      <text class="copy center" x="1385" y="1043" font-size="14">10mL / 0.33 fl. oz</text>
    </g>

    <g class="panel-directions">
      <rect class="label-bar" x="1497" y="545" width="16" height="163"/>
      <text class="bar-text" transform="translate(1509,704) rotate(-90)" font-size="11">CAUTION:</text>
      <text class="copy" transform="translate(1527,708) rotate(-90)" font-size="10">
        <tspan x="0" y="0">Possible skin sensitivity. Keep out of reach of</tspan>
        <tspan x="0" dy="15">children. Not for ingestion or internal use. Avoid</tspan>
        <tspan x="0" dy="15">contact with eyes, inner ears and sensitive areas.</tspan>
      </text>
      <rect class="label-bar" x="1497" y="810" width="16" height="162"/>
      <text class="bar-text" transform="translate(1509,968) rotate(-90)" font-size="11">DIRECTIONS:</text>
      <text class="copy" transform="translate(1527,972) rotate(-90)" font-size="10">
        <tspan x="0" y="0">Apply directly onto skin. For sensitive skin,</tspan>
        <tspan x="0" dy="15">dilute with a carrier oil (such as jojoba or</tspan>
        <tspan x="0" dy="15">coconut) before application.</tspan>
      </text>
      <circle class="brand-dot" cx="1493" cy="1030" r="12" stroke-width="3"/>
      <text class="brand" x="1511" y="1027" font-size="17">DUSK</text>
      <text class="brand" x="1511" y="1043" font-size="17">HAVEN</text>
    </g>

    <g class="panel-info">
      <text class="copy center" font-size="11">
        <tspan x="1671" y="447">Essential Oils have been</tspan>
        <tspan x="1671" dy="14">used for centuries to</tspan>
        <tspan x="1671" dy="14">help prepare the mind</tspan>
        <tspan x="1671" dy="14">and body for sleep.</tspan>
        <tspan x="1671" dy="28">Dusk Haven contain a</tspan>
        <tspan x="1671" dy="14">balanced blend of the</tspan>
        <tspan x="1671" dy="14">most sleep supporting</tspan>
        <tspan x="1671" dy="14">essential oils.</tspan>
        <tspan x="1671" dy="28"><tspan class="strong">Lavender</tspan> for restfulness</tspan>
        <tspan x="1671" dy="14.5"><tspan class="strong">Vetiver</tspan> for grounding</tspan>
        <tspan x="1671" dy="14.5"><tspan class="strong">Cedarwood</tspan> for relaxation</tspan>
        <tspan x="1671" dy="14.5"><tspan class="strong">Marjoram</tspan> for balance</tspan>
        <tspan x="1671" dy="14.5"><tspan class="strong">Roman Chamomile</tspan> for</tspan>
        <tspan x="1671" dy="14.5">comfort</tspan>
        <tspan x="1671" dy="28">Add Dusk Haven to</tspan>
        <tspan x="1671" dy="14">your nightly bedtime</tspan>
        <tspan x="1671" dy="14">ritual to help support</tspan>
        <tspan x="1671" dy="14">you in achieving deep</tspan>
        <tspan x="1671" dy="14">and rejuvenating sleep.</tspan>
      </text>
      <rect class="brand-dot" x="1656" y="809" width="30" height="30" stroke-width="3.5"/>
      <text class="copy center" x="1671" y="850" font-size="11">@duskhavenau</text>
      <text class="copy center" x="1671" y="919" font-size="11">Visit</text>
      <rect class="label-bar" x="1607" y="923" width="127" height="13"/>
      <text class="bar-text center" x="1671" y="933" font-size="10">www.duskhaven.com.au</text>
      <text class="copy center" x="1671" y="946" font-size="11">to learn more</text>
      <use href="#open-jar" x="1629" y="1009" width="38" height="32"/>
      <use href="#recycle-mark" x="1676" y="1008" width="34" height="34"/>
    </g>
  </g>

  <!-- ================= 5 mL roll-on box ================= -->
  <g class="box box-5ml">
    <path class="dieline" d="M2002,521 V366 Q2002,354 2014,354 H2126 Q2138,354 2138,366 V521
      M2002,435 H1895 L1880,510 Q1868,513 1868,521 L1831,536 V945 L1868,963 Q1868,971 1880,975 L1895,1048 H2002
      M2002,963 V1118 Q2002,1130 2014,1130 H2126 Q2138,1130 2138,1118 V963
      M2138,435 H2240 L2258,510 Q2272,513 2272,521
      M2138,1048 H2240 L2258,975 Q2272,971 2272,963
      M2002,390 h12 M2126,390 h12 M2002,1095 h12 M2126,1095 h12"/>
    <path class="fold" d="M1868,521 H2272 M1868,963 H2272"/>
    <rect class="dieline" x="2272" y="521" width="136" height="444"/>
    <circle class="tab-ring" cx="2070" cy="455" r="42" stroke-width="7"/>
    <circle class="tab-ring" cx="2070" cy="1030" r="42" stroke-width="7"/>

    <g class="panel-ingredients">
      <circle class="brand-dot" cx="1897" cy="935" r="14" stroke-width="3.5"/>
      <text class="brand" transform="translate(1895,910) rotate(-90)" font-size="22" letter-spacing="1">
        <tspan x="0" y="0">DUSK</tspan><tspan x="0" dy="20">HAVEN</tspan>
      </text>
      <rect class="label-bar" x="1921" y="812" width="14" height="138"/>
      <text class="bar-text" transform="translate(1932,946) rotate(-90)" font-size="10">INGREDIENTS:</text>
      <text class="copy" transform="translate(1949,950) rotate(-90)" font-size="9">
        <tspan x="0" y="0">Lavandula Angustifolia (Australian Lavender), Vetiveria Zizanoides (Vetiver) Root Oil, Sweet Vanilla</tspan>
        <tspan x="0" dy="11">Fragrant Oil, Pelargonium Capitatum (Cape Rose Geranium) Leaf Extract, Juniperus Virginiana</tspan>
        <tspan x="0" dy="11">(Cedarwood) Wood Oil, Citrus Limon (Australian Lemon) Peel Oil, Origanum Majorana (Marjoram)</tspan>
        <tspan x="0" dy="11">Leaf Oil, Cananga Odorata (Ylang Ylang) Flower Oil, Anthemis Nobilis (Roman Chamomile) Flower Oil.</tspan>
      </text>
    </g>

    <g class="panel-front">
      <circle class="brand-dot" cx="2070" cy="650" r="28" stroke-width="5"/>
      <text class="brand center" x="2070" y="720" font-size="35" letter-spacing="2">DUSK</text>
      <text class="brand center" x="2070" y="740" font-size="15" letter-spacing="8">HAVEN</text>
      <text class="copy center" x="2070" y="770" font-size="13">Roll on</text>
      <rect class="label-bar" x="2013" y="773" width="113" height="13"/>
      <text class="bar-text center" x="2070" y="783" font-size="11">Essential Oil Blend</text>
      <text class="copy center" x="2070" y="932" font-size="12">Made in Australia</text>
      <text class="copy center" x="2070" y="949" font-size="12">5mL / 0.17 fl. oz</text>
    </g>

    <g class="panel-directions">
      <rect class="label-bar" x="2167" y="555" width="16" height="135"/>
      <text class="bar-text" transform="translate(2179,686) rotate(-90)" font-size="10">CAUTION:</text>
      <text class="copy" transform="translate(2197,690) rotate(-90)" font-size="9">
        <tspan x="0" y="0">Possible skin sensitivity. Keep out of</tspan>
        <tspan x="0" dy="13">reach of children. Not for ingestion</tspan>
        <tspan x="0" dy="13">or internal use. Avoid contact with</tspan>
        <tspan x="0" dy="13">eyes, inner ears and sensitive areas.</tspan>
      </text>
      <rect class="label-bar" x="2167" y="750" width="16" height="138"/>
      <text class="bar-text" transform="translate(2179,884) rotate(-90)" font-size="10">DIRECTIONS:</text>
      <text class="copy" transform="translate(2197,888) rotate(-90)" font-size="9">
        <tspan x="0" y="0">Apply directly onto skin. For sensitive</tspan>
        <tspan x="0" dy="13">skin, dilute with a carrier oil (such as</tspan>
        <tspan x="0" dy="13">jojoba or coconut) before application.</tspan>
      </text>
      <circle class="brand-dot" cx="2166" cy="937" r="11" stroke-width="3"/>
      <text class="brand" x="2184" y="935" font-size="16">DUSK</text>
      <text class="brand" x="2184" y="950" font-size="16">HAVEN</text>
    </g>

    <g class="panel-info">
      <text class="copy center" font-size="9">
        <tspan x="2340" y="545">Essential Oils have been</tspan>
        <tspan x="2340" dy="12">used for centuries to</tspan>
        <tspan x="2340" dy="12">help prepare the mind</tspan>
        <tspan x="2340" dy="12">and body for sleep.</tspan>
        <tspan x="2340" dy="25">Dusk Haven contain a</tspan>
        <tspan x="2340" dy="12">balanced blend of the</tspan>
        <tspan x="2340" dy="12">most sleep supporting</tspan>
        <tspan x="2340" dy="12">essential oils.</tspan>
        <tspan x="2340" dy="25"><tspan class="strong">Lavender</tspan> for restfulness</tspan>
        <tspan x="2340" dy="12.5"><tspan class="strong">Vetiver</tspan> for grounding</tspan>
        <tspan x="2340" dy="12.5"><tspan class="strong">Cedarwood</tspan> for relaxation</tspan>
        <tspan x="2340" dy="12.5"><tspan class="strong">Marjoram</tspan> for balance</tspan>
        <tspan x="2340" dy="12.5"><tspan class="strong">Roman Chamomile</tspan> for</tspan>
        <tspan x="2340" dy="12.5">comfort</tspan>
        <tspan x="2340" dy="25">Add Dusk Haven to</tspan>
        <tspan x="2340" dy="12.5">your nightly bedtime</tspan>
        <tspan x="2340" dy="12.5">ritual to help support</tspan>
        <tspan x="2340" dy="12.5">you in achieving deep</tspan>
        <tspan x="2340" dy="12.5">and rejuvenating sleep.</tspan>
      </text>
      <rect class="brand-dot" x="2326" y="817" width="28" height="28" stroke-width="3.5"/>
      <text class="copy center" x="2340" y="859" font-size="10">@duskhavenau</text>
      <text class="copy center" x="2340" y="883" font-size="9">Visit</text>
      <rect class="label-bar" x="2282" y="886" width="116" height="12"/>
      <text class="bar-text center" x="2340" y="895" font-size="9">www.duskhaven.com.au</text>
      <text class="copy center" x="2340" y="907" font-size="9">to learn more</text>
      <use href="#open-jar" x="2304" y="925" width="34" height="28"/>
      <use href="#recycle-mark" x="2343" y="923" width="28" height="28"/>
    </g>
  </g>
</svg>
</div>
</body>
</html>
```